Professional violinist needs business cards

I am trying to attract the following jobs:
-private violin lessons (primarily classical)
-performance gigs (weddings, birthday parties, funerals, etc.)
-collaborations with other artists (studio recordings, performances)

I want to communicate that I have a very high standard of excellence for my work, but I also love people and celebrations.
Values/style words I like are:
love, joy, peace, fun, beauty, authenticity, excellence, warmth, refined/sleek, free spirited. If that's too confusing, just ignore :)

I will attach my favorite business card template that I could find on Canva. The lines are supposed to be like a music staff, which I think is really cool, but I also don't want it to look too busy. I like the simple black and white--I think it looks sharp--but I also am open to other ideas. I also have seen business cards with pictures included that looked great, so I attached an image that could be used as well.

I am also attaching a file that I made of my initials that could be used as a logo, but I'm not sure if it should be included.

Information on the card:
-My name (18 letters total)
-"violinist"
-phone number, email, website

Thank you!

```html
<!DOCTYPE html>
<html lang="en">
<head>
<meta charset="utf-8">
<title>Marianne Holloway – Violinist Business Cards</title>
<link href="https://fonts.googleapis.com/css2?family=Crimson+Pro:wght@400;600&display=swap" rel="stylesheet">
<style>
  :root {
    --stage: #3a3a3a;
    --stage-dark: #1e1e1e;
    --card: #000000;
    --ink: #ffffff;
    --panel: #ffffff;
    --photo-stone: #8a8273;
    --photo-deep: #4a4238;
  }
  * { margin: 0; padding: 0; box-sizing: border-box; }
  html, body { width: 1200px; height: 1200px; overflow: hidden; }
  body {
    background: radial-gradient(circle at 50% 45%, var(--stage) 0%, var(--stage-dark) 100%);
    font-family: "Crimson Pro", Georgia, serif;
    color: var(--ink);
    position: relative;
  }
  .card {
    position: absolute;
    left: 160px;
    width: 880px;
    height: 503px;
    background: var(--card);
    border-radius: 36px;
    overflow: hidden;
  }
  .card--front { top: 70px; }
  .card--back { top: 627px; }
  .card-art { position: absolute; inset: 0; width: 880px; height: 503px; }

  .identity {
    position: absolute;
    left: 450px;
    right: 40px;
    top: 170px;
  }
  .identity__name { font-size: 44px; font-weight: 600; letter-spacing: 0.5px; line-height: 1; white-space: nowrap; }
  .identity__title { font-size: 24px; letter-spacing: 2px; margin-top: 10px; }
  .contact { list-style: none; margin-top: 38px; }
  .contact__item {
    display: flex; align-items: center; gap: 14px;
    font-size: 25px; line-height: 1.35; white-space: nowrap;
  }
  .contact__icon { width: 24px; height: 24px; flex: none; }

  .back-content {
    position: absolute;
    left: 0; top: 0;
    width: 520px; height: 503px;
    display: flex; flex-direction: column; align-items: center;
    padding-top: 110px;
  }
  .brand-name {
    font-size: 56px; font-weight: 400; line-height: 1.05; text-align: center;
  }
  .services {
    list-style: none; margin-top: 48px; text-align: center;
    font-size: 23px; letter-spacing: 1px; line-height: 1.25; text-transform: uppercase;
  }
  .social {
    margin-top: 44px; display: flex; align-items: center; gap: 12px;
    font-size: 22px;
  }
  .social__dot { width: 22px; height: 22px; border-radius: 50%; background: var(--ink); }
</style>
</head>
<body>

<section class="card card--front" aria-label="Business card front">
  <svg class="card-art" viewBox="0 0 880 503">
    <defs>
      <linearGradient id="panelShade" x1="0" y1="0" x2="1" y2="0">
        <stop offset="0" stop-color="#ffffff"/>
        <stop offset="0.55" stop-color="#e6e6e6"/>
        <stop offset="1" stop-color="#ffffff"/>
      </linearGradient>
    </defs>
    <path role="img" aria-label="Black silhouette of a woman playing the violin inside a white violin-shaped panel"
      fill="url(#panelShade)"
      d="M0 0 H360 C370 60 330 110 345 160 C360 200 400 215 390 260 C380 300 350 320 360 360 C372 410 400 450 380 503 H0 Z"/>
  </svg>
  <div class="identity">
    <h1 class="identity__name">Marianne Holloway</h1>
    <p class="identity__title">VIOLINIST</p>
    <ul class="contact">
      <li class="contact__item">
        <svg class="contact__icon" viewBox="0 0 24 24"><circle cx="12" cy="12" r="11" fill="#fff"/><path d="M8 6l2 3-1.5 1.5c.8 2 2.2 3.4 4 4L14 13l3 2-1.2 2.5C11 17 7 13 6.5 8.2Z" fill="#000"/></svg>
        (555) 214 7730
      </li>
      <li class="contact__item">
        <svg class="contact__icon" viewBox="0 0 24 24"><rect x="2" y="5" width="20" height="14" fill="#fff"/><path d="M2 5l10 8 10-8" fill="none" stroke="#000" stroke-width="1.6"/></svg>
        hello@mholloway.com
      </li>
      <li class="contact__item">
        <svg class="contact__icon" viewBox="0 0 24 24"><circle cx="12" cy="12" r="10" fill="none" stroke="#fff" stroke-width="2"/><ellipse cx="12" cy="12" rx="4.5" ry="10" fill="none" stroke="#fff" stroke-width="1.6"/><path d="M2 12h20" stroke="#fff" stroke-width="1.6"/></svg>
        www.mholloway.com
      </li>
    </ul>
  </div>
</section>

<section class="card card--back" aria-label="Business card back">
  <svg class="card-art" viewBox="0 0 880 503">
    <defs>
      <linearGradient id="photoTone" x1="0" y1="0" x2="1" y2="1">
        <stop offset="0" stop-color="#8a8273"/>
        <stop offset="1" stop-color="#4a4238"/>
      </linearGradient>
    </defs>
    <path role="img" aria-label="Photo of the violinist in a black dress holding her violin and bow against a stone wall"
      fill="url(#photoTone)"
      d="M600 0 H760 C770 50 740 90 755 140 C768 180 800 200 790 250 C780 300 750 320 760 360 C772 410 790 450 780 503 H520 C535 460 560 430 555 390 C548 340 515 320 525 270 C535 220 580 200 585 150 C590 100 585 50 600 0 Z"/>
  </svg>
  <div class="back-content">
    <p class="brand-name">Marianne<br>Holloway</p>
    <ul class="services">
      <li>-Private Violin Lessons</li>
      <li>-Performance Gigs</li>
      <li>-Collaborations with Other Artists</li>
    </ul>
    <p class="social"><span class="social__dot"></span>@mhollowayviolin</p>
  </div>
</section>

</body>
</html>
```